Corvane Summit 2018 Conference flyer

We require a professionally designed flyer for printing and soft copy distributing. The current flyer attached with the information that is required. We need a modern, eye catching flyer to accompany the banner. The banner should represent what the conference is all about. We require the Corvane Lab colours as featured in the current banner. The information needs to be legible and well spaced out so people can find the information quickly.

Target Market(s)

Relating to healthcare professionals, scientists, engineers

Font styles to use
Sans Serif

```html
<!DOCTYPE html>
<html lang="en">
<head>
<meta charset="utf-8">
<title>Corvane Summit 2018 Conference</title>
<link rel="stylesheet" href="https://fonts.googleapis.com/css2?family=Oswald:wght@300;500&family=Ubuntu:wght@400;700&family=Open+Sans:wght@400;600;700&display=swap">
<style>
  :root {
    --pink: #e6176f;
    --navy: #0c2456;
    --navy-deep: #08183d;
    --blue: #1d5aa6;
    --white: #ffffff;
    --ink: #1f2a44;
    --grey-ink: #2b2f3a;
  }
  * { margin: 0; padding: 0; box-sizing: border-box; }
  html, body { width: 896px; height: 1200px; overflow: hidden; background: #f2f2f2; }
  .flyer {
    position: relative; width: 896px; height: 1200px; overflow: hidden;
    background: linear-gradient(180deg, var(--blue) 0%, var(--navy) 55%, var(--navy-deep) 100%);
    font-family: "Open Sans", sans-serif;
  }
  .band { position: absolute; left: 0; width: 100%; background: var(--pink); }
  .band--top { top: 0; height: 20px; }
  .band--bottom { bottom: 0; height: 20px; }

  .title-block {
    position: absolute; left: 0; top: 20px; width: 321px; height: 226px;
    background: linear-gradient(160deg, var(--navy-deep), var(--navy) 60%, var(--blue));
    color: var(--white); text-align: center; padding-top: 34px;
  }
  .title-block__main { font-family: "Oswald", sans-serif; font-weight: 500; font-size: 76px; line-height: 1; letter-spacing: 1px; }
  .title-block__sub { font-family: "Oswald", sans-serif; font-weight: 300; font-size: 42px; line-height: 1.2; margin-top: 10px; }

  .event-details {
    position: absolute; left: 321px; top: 20px; width: 575px; height: 226px;
    background: var(--white); padding: 36px 0 0 28px; font-family: "Ubuntu", sans-serif;
  }
  .event-details__date { color: var(--pink); font-weight: 700; font-size: 26px; margin-bottom: 8px; }
  .event-details__venue { color: var(--ink); font-size: 23px; line-height: 1.3; }
  .event-details__time { color: var(--pink); font-size: 23px; margin-top: 10px; letter-spacing: 1px; }

  .hero-photo {
    position: absolute; left: 0; top: 246px; width: 896px; height: 474px;
    border-bottom-right-radius: 46px;
    background: radial-gradient(circle at 30% 30%, #d8dde2 0%, #b9c0c7 40%, #6d7485 70%, #1f2f6e 100%);
  }

  .info-panel {
    position: absolute; left: 312px; top: 720px; width: 584px; height: 367px;
    background: var(--white); border-bottom-left-radius: 64px; padding: 22px 22px 0 30px;
  }
  .info-panel__intro { color: var(--pink); font-size: 17px; line-height: 1.5; }
  .agenda { list-style: none; margin-top: 16px; }
  .agenda__item { display: flex; gap: 10px; color: var(--grey-ink); font-size: 17.5px; line-height: 1.5; margin-bottom: 2px; }
  .agenda__item svg { flex: none; margin-top: 6px; }

  .partners { position: absolute; left: 40px; right: 14px; bottom: 34px; display: flex; align-items: center; justify-content: space-between; }
  .partner { display: flex; align-items: center; gap: 7px; color: var(--navy); font-weight: 600; font-size: 19px; }
  .partner__dot { width: 14px; height: 14px; border-radius: 50%; background: var(--navy); }

  .badge {
    position: absolute; left: 44px; top: 592px; width: 236px; height: 236px; border-radius: 50%;
    background: var(--white); display: flex; flex-direction: column; align-items: center; justify-content: center;
    color: var(--navy); font-weight: 700; text-align: center; font-size: 26px; line-height: 1.15;
  }

  .offer { position: absolute; left: 0; width: 312px; top: 862px; text-align: center; color: var(--white); }
  .offer__label { font-weight: 700; font-size: 24px; }
  .offer__headline { font-family: "Oswald", sans-serif; font-weight: 500; font-size: 52px; line-height: 1.15; margin-top: 4px; }
  .offer__note { font-size: 21px; margin-top: 2px; }
  .offer__code {
    display: inline-block; margin-top: 10px; width: 234px; height: 42px; line-height: 38px;
    background: var(--pink); border: 2px solid var(--white); border-radius: 22px;
    font-weight: 700; font-size: 27px; letter-spacing: 1px;
  }

  .contact-bar { position: absolute; left: 0; width: 100%; top: 1130px; text-align: center; font-size: 14px; color: var(--white); }
  .contact-bar__label { color: var(--pink); }
</style>
</head>
<body>
<div class="flyer">
  <div class="band band--top"></div>

  <header class="title-block">
    <div class="title-block__main">CORVANE</div>
    <div class="title-block__sub">SUMMIT 2018</div>
  </header>

  <section class="event-details">
    <p class="event-details__date">Saturday 13 &amp; Sunday 14 October 2018</p>
    <p class="event-details__venue">Eastbrook Neuro Centre<br>Ardell Building 52 Linden Parade<br>FERNVALE&nbsp; VIC&nbsp; 3999</p>
    <p class="event-details__time">Starting at 09:00hrs</p>
  </section>

  <div class="hero-photo" role="img" aria-label="Photograph of colourful 3D printed anatomical models: red blood vessels, a heart, a kidney and a blue prosthetic hand"></div>

  <section class="info-panel">
    <p class="info-panel__intro">The @CorvaneLab at Harlow Health warmly invites you to attend the 2018 Corvane Summit Symposium.<br>This cross-disciplinary event will:</p>
    <ul class="agenda">
      <li class="agenda__item"><svg width="14" height="14" viewBox="0 0 14 14"><circle cx="7" cy="7" r="6" fill="none" stroke="#e6176f" stroke-width="1.5"/><path d="M4 7.2l2 2 4-4.2" fill="none" stroke="#e6176f" stroke-width="1.5"/></svg>Showcase clinical applications of 3d modelling &amp; printing</li>
      <li class="agenda__item"><svg width="14" height="14" viewBox="0 0 14 14"><circle cx="7" cy="7" r="6" fill="none" stroke="#e6176f" stroke-width="1.5"/><path d="M4 7.2l2 2 4-4.2" fill="none" stroke="#e6176f" stroke-width="1.5"/></svg>Explore the use of Virtual Reality in Medicine</li>
      <li class="agenda__item"><svg width="14" height="14" viewBox="0 0 14 14"><circle cx="7" cy="7" r="6" fill="none" stroke="#e6176f" stroke-width="1.5"/><path d="M4 7.2l2 2 4-4.2" fill="none" stroke="#e6176f" stroke-width="1.5"/></svg>Bring together clinicians, engineers and thought leaders in medical 3D printing</li>
      <li class="agenda__item"><svg width="14" height="14" viewBox="0 0 14 14"><circle cx="7" cy="7" r="6" fill="none" stroke="#e6176f" stroke-width="1.5"/><path d="M4 7.2l2 2 4-4.2" fill="none" stroke="#e6176f" stroke-width="1.5"/></svg>Discuss social and legal issues in medical 3d printing</li>
    </ul>
    <div class="partners">
      <span class="partner">Printwell</span>
      <span class="partner"><span class="partner__dot"></span>Harlow Health</span>
      <span class="partner">Westmere University</span>
    </div>
  </section>

  <div class="badge">Corvane<br>Summit 2018</div>

  <section class="offer">
    <p class="offer__label">DISCOUNT CODE:</p>
    <p class="offer__headline">GET 50% OFF</p>
    <p class="offer__note">your ticket if you enter</p>
    <span class="offer__code">3DPROMO</span>
  </section>

  <footer class="contact-bar">
    <span class="contact-bar__label">More info:</span> corvanelab.org/summit18/ <span class="contact-bar__label">| Registration:</span> corvanelab.org/register/ <span class="contact-bar__label">| Enquiries:</span> lab@harlowhealth.org
  </footer>

  <div class="band band--bottom"></div>
</div>
</body>
</html>
```